Business Card, Stationary with Shark Logo for Personal Injury Lawyer

I need business cards and stationery with a shark logo for my Personal Injury Law Practice. Has to have this written on it:
Martin K. Hollis
Injury Lawyer
The Corvell Building
718 Tandy Street
Providence, Rhode Island 02908
401-627-4193
Martinhollis.com

Contact Information for Business Card

Martin K. Hollis, Injury Lawyer, address, 401-627-4193, martinhollis.com

```html
<!DOCTYPE html>
<html lang="en">
<head>
<meta charset="utf-8">
<title>Martin K. Hollis – Business Card</title>
<link rel="stylesheet" href="https://fonts.googleapis.com/css2?family=Roboto+Condensed:wght@700&family=Open+Sans:wght@400&display=swap">
<style>
  :root {
    --page: #e9e9ea;
    --card-white: #f7f7f9;
    --navy: #2b2766;
    --navy-deep: #221f59;
    --navy-ink: #1c1948;
    --grey-text: #6b6b6b;
    --body-text: #3a3a44;
  }
  * { margin: 0; padding: 0; box-sizing: border-box; }
  html, body {
    width: 1200px; height: 1200px; overflow: hidden;
    background: var(--page);
  }
  .sheet { position: relative; width: 1200px; height: 1200px; }

  .card {
    position: absolute;
    left: 257px;
    width: 686px; height: 392px;
    border-radius: 20px;
    overflow: hidden;
  }
  .card--front { top: 165px; background: var(--card-white); }
  .card--back  { top: 653px; background: linear-gradient(180deg, #322e6b 0%, var(--navy-deep) 100%); }

  .brand-name {
    position: absolute; left: 51px; top: 52px;
    font-family: "Roboto Condensed", sans-serif; font-weight: 700;
    font-size: 44px; line-height: 1.02; letter-spacing: 0.5px;
    color: var(--navy); text-transform: uppercase;
  }

  .holder { position: absolute; left: 51px; top: 152px; }
  .holder__title {
    font-family: "Roboto Condensed", sans-serif; font-weight: 700;
    font-size: 22px; color: var(--navy); letter-spacing: 3px;
    text-transform: uppercase;
  }

  .contact { position: absolute; left: 51px; top: 222px; list-style: none; }
  .contact__item {
    display: flex; align-items: center; gap: 8px;
    font-family: "Open Sans", sans-serif; font-size: 14px;
    color: var(--body-text); line-height: 22px;
  }
  .contact__item--cont { padding-left: 22px; }
  .contact__icon { width: 14px; height: 14px; flex: none; }

  .fin-art {
    position: absolute; left: 400px; top: 48px;
    width: 286px; height: 344px;
  }

  .back-name {
    position: absolute; left: 0; right: 0; top: 50%;
    transform: translateY(-50%);
    text-align: center;
    font-family: "Roboto Condensed", sans-serif; font-weight: 700;
    font-size: 66px; line-height: 1.05; letter-spacing: 1px;
    color: var(--navy-ink); text-transform: uppercase;
  }
</style>
</head>
<body>
<main class="sheet">

  <section class="card card--front" aria-label="Business card front">
    <h1 class="brand-name">Martin K.<br>Hollis</h1>

    <div class="holder">
      <p class="holder__title">Injury Lawyer</p>
    </div>

    <ul class="contact">
      <li class="contact__item">
        <svg class="contact__icon" viewBox="0 0 14 14" aria-hidden="true">
          <path d="M7 0.5 C4.2 0.5 2.5 2.6 2.5 5 C2.5 8.5 7 13.5 7 13.5 C7 13.5 11.5 8.5 11.5 5 C11.5 2.6 9.8 0.5 7 0.5 Z" fill="var(--navy)"/>
          <circle cx="7" cy="5" r="1.8" fill="#fff"/>
        </svg>
        The Corvell Building, 718 Tandy Street
      </li>
      <li class="contact__item contact__item--cont">Providence, Rhode Island 02908</li>
      <li class="contact__item">
        <svg class="contact__icon" viewBox="0 0 14 14" aria-hidden="true">
          <path d="M3 0.8 L5.2 0.8 L6.2 3.8 L4.6 5 C5.4 6.8 7.2 8.6 9 9.4 L10.2 7.8 L13.2 8.8 L13.2 11 C13.2 12.2 12.2 13.2 11 13.2 C5.5 12.8 1.2 8.5 0.8 3 C0.8 1.8 1.8 0.8 3 0.8 Z" fill="var(--navy)"/>
        </svg>
        401-627-4193
      </li>
      <li class="contact__item">
        <svg class="contact__icon" viewBox="0 0 14 14" aria-hidden="true">
          <rect x="0.5" y="2.5" width="13" height="9" fill="var(--navy)"/>
          <path d="M1 3 L7 8 L13 3" fill="none" stroke="#fff" stroke-width="1.2"/>
        </svg>
        Martin@martinhollis.com
      </li>
      <li class="contact__item">
        <svg class="contact__icon" viewBox="0 0 14 14" aria-hidden="true">
          <circle cx="7" cy="7" r="6.5" fill="var(--navy)"/>
          <path d="M4 4.5 Q6 3.5 7 5 Q6 7 4.5 7.5 Z M8 8 Q10 8 10 10 Q8.5 11.5 7.5 10 Z" fill="#fff"/>
        </svg>
        Martinhollis.com
      </li>
    </ul>

    <svg class="fin-art" viewBox="0 0 286 344" role="img" aria-label="Large shark fin illustration">
      <defs>
        <linearGradient id="finTone" x1="0" y1="0" x2="0" y2="1">
          <stop offset="0" stop-color="#34307a"/>
          <stop offset="1" stop-color="#231f5c"/>
        </linearGradient>
      </defs>
      <rect x="0" y="0" width="286" height="344" fill="url(#finTone)"/>
    </svg>
  </section>

  <section class="card card--back" aria-label="Business card back">
    <div class="back-name">Martin K.<br>Hollis</div>
  </section>

</main>
</body>
</html>
```